KW Sports & Remedial Massage needs a new logo & business card design

The design is for my Sports and remedial massage business. My business is aimed at everyone who has a muscle ache or injury so not just sports related. I need a design which is sharp, clear and professional. No greens, or pastel colours or floral/girly designs. Perhaps just a Navy background and white text or other way around or perhaps grey. I want to make it clear that I treat everyone and not just sporty people.

Target Market(s)

People with muscle aches or sports injuries

Industry/Entity Type

Health And Wellness

Contact Information for Business Card

It needs to also include the following:
Name: Marion Kebbell
Mobile No: 07432 519 268
Email: marionkebbell@postvane.com
Qualifications: Dip SM, Dip SRM

Logo Text

KW Sports & Remedial Massage

Font styles to use
Serif
Other font styles liked:
• Tahoma, Verdana

Colors
5c5c5c
7f7f7f
9d9d9d
0255a3
3176b5
85abd2

Requirements
Must have
• I was thinking of a few simple people figures at the bottom of the card to highlight this i.e. a gardener, musician mixed in with a cyclist and tennis player.
Should not have
• Anything which indicates beauty therapy or relaxing. I am there to get rid of aches and pains and often to give rehab to certain injuries.

```html
<!DOCTYPE html>
<html lang="en">
<head>
<meta charset="utf-8">
<title>Marion Kebbell – Business Card</title>
<link rel="stylesheet" href="https://fonts.googleapis.com/css2?family=Open+Sans:wght@400&display=swap">
<style>
  :root {
    --brand-blue: #1274bc;
    --swoosh-grey: #bdbec1;
    --card-edge: #3a3a3a;
    --paper: #ffffff;
    --figure-blue: #2a7cc0;
    --figure-grey: #c9cacd;
  }
  html, body {
    margin: 0;
    padding: 0;
    width: 1200px;
    height: 846px;
    overflow: hidden;
    background: var(--paper);
  }
  .canvas {
    position: relative;
    width: 1200px;
    height: 846px;
  }
  .business-card {
    position: absolute;
    left: 0;
    top: 0;
    width: 1200px;
    height: 846px;
    font-family: "Open Sans", Tahoma, Verdana, sans-serif;
  }
  .contact-text {
    fill: var(--brand-blue);
    font-size: 24px;
  }
  .holder-name {
    fill: var(--paper);
    font-size: 49px;
    letter-spacing: 0.5px;
  }
  .qualifications {
    fill: var(--paper);
    font-size: 28px;
  }
  .player-figure-area {
    position: absolute;
    left: 191px;
    top: 180px;
    width: 333px;
    height: 398px;
    border-radius: 50%;
    background: radial-gradient(ellipse at 55% 45%, var(--figure-blue) 0%, var(--figure-blue) 35%, var(--figure-grey) 75%, rgba(201,202,205,0) 100%);
    opacity: 0.85;
  }
</style>
</head>
<body>
<div class="canvas">
  <svg class="business-card" viewBox="0 0 1200 846" xmlns="http://www.w3.org/2000/svg">
    <defs>
      <clipPath id="card-clip">
        <rect x="148" y="133" width="888" height="520"/>
      </clipPath>
    </defs>

    <rect class="card-face" x="148" y="133" width="888" height="520" fill="var(--paper)"/>

    <g class="circle-panel" clip-path="url(#card-clip)">
      <circle cx="873" cy="393" r="308" fill="var(--swoosh-grey)"/>
      <circle cx="908" cy="393" r="302" fill="var(--brand-blue)"/>
    </g>

    <rect class="card-border" x="148" y="133" width="888" height="520" fill="none" stroke="var(--card-edge)" stroke-width="1"/>

    <g class="phone-line">
      <g class="icon-phone" fill="var(--brand-blue)">
        <rect x="177" y="151" width="16" height="27" rx="3"/>
        <rect x="181" y="155" width="8" height="8" rx="1" fill="var(--paper)"/>
        <circle cx="185" cy="171" r="2" fill="var(--paper)"/>
      </g>
      <text class="contact-text" x="214" y="174">07432 519 268</text>
    </g>

    <g class="email-line">
      <g class="icon-mail" fill="none" stroke="var(--brand-blue)" stroke-width="3">
        <rect x="174" y="606" width="32" height="20"/>
        <polyline points="174,606 190,619 206,606"/>
      </g>
      <text class="contact-text" x="219" y="624">marionkebbell@postvane.com</text>
    </g>

    <g class="holder-details">
      <text class="holder-name" x="625" y="407">Marion Kebbell</text>
      <text class="qualifications" x="715" y="456">Dip SM, Dip SRM</text>
    </g>
  </svg>

  <div class="player-figure-area" role="img" aria-label="Blue silhouette of a tennis player serving, framed by a grey swoosh"></div>
</div>
</body>
</html>
```